B2B telecom company need web design

We need a web design for our corporate web site. The company exists since almost 10 years.
This is a DESIGN contest, you're expected to provide design only, NOT the whole website. The winner will have to provide the HTML template (with Lorem Ipsum content) and the CSS files of his design.
Our initial product is SMS peering in P2P (you send a SMS to a friend in a foreign country, great chance that your operator route your SMS to us that we route to the recipient). We're launching a bulk SMS service (marketing and application to SMS).
Target is mostly corporate, usually big corporate (operators, contents providers...) where use of SMS is part of the main business.
The web site is composed of 1 landing page and 7 content pages (plan is given for your information, all content page are using the same template and the same design, you do NOT need to make one design per page) :
* About US
Company Profile
They trust us
The Vortel Team
Partners
Contact us
* Solution
P2P SMS
A2P SMS
You only need to submit the landing page and a template page for the content (with h1, h2, h3 and h4).
Design must be based on our new logo (see attached file).
Our current web site http://www.vortel-example.com
The winner of the contest will have to provide state of the art HTML template and CSS files of his design. Photo used shall be downloaded from Pixaldo (provide the ID of the picture that we purchase file).
Target Market(s)
Telecom operator. SMS Peering hubs. Bulk SMS.
Industry/Entity Type
It Company
Number of Pages Required
2 page
Look and feel

```html
<!DOCTYPE html>
<html lang="en">
<head>
<meta charset="utf-8">
<title>Vortel Mobile</title>
<link href="https://fonts.googleapis.com/css2?family=Titillium+Web:wght@300;400;600;700&family=Roboto:wght@400;500;700&display=swap" rel="stylesheet">
<style>
:root{
  --green:#8dc21f;
  --green-dark:#7aab17;
  --dark:#232323;
  --footer:#2e2e2e;
  --panel:#f7f7f7;
  --text:#3a3a3a;
  --muted:#d8d8d8;
  --white:#ffffff;
}
*{margin:0;padding:0;box-sizing:border-box}
html,body{width:688px;height:1200px;overflow:hidden;background:var(--white)}
body{position:relative;font-family:Arial,Helvetica,sans-serif;color:var(--text)}
.abs{position:absolute}
.header{left:0;top:0;width:688px;height:78px;background:var(--dark)}
.brand{left:54px;top:14px;font-family:'Titillium Web',sans-serif;font-size:18px;font-weight:600;color:var(--white);letter-spacing:1px;display:flex;align-items:center;gap:6px}
.brand .dot{width:8px;height:8px;border-radius:50%;background:var(--green)}
.call{right:64px;top:17px;font-family:'Titillium Web',sans-serif;font-size:13px;color:var(--white);display:flex;align-items:center;gap:6px}
.call b{color:var(--green);font-weight:600;font-size:10.5px}
.nav{left:54px;top:50px;width:580px;height:28px;background:var(--green);border:2px solid var(--white);border-bottom:none;display:flex;align-items:center;padding-left:12px}
.nav a{font-family:'Roboto',sans-serif;font-size:7px;font-weight:500;color:#1d2a05;text-decoration:none;padding:0 13px;border-right:1px solid #a8d455;letter-spacing:.2px}
.nav a:last-child{border-right:none}
.hero{left:55px;top:78px;width:579px;height:218px;background:linear-gradient(100deg,#b9bfc2 0%,#d7dadb 35%,#cfd2cf 55%,#9a9e9c 80%,#6f7370 100%)}
.hero-title{left:75px;top:122px;font-family:'Roboto',sans-serif;font-weight:700;font-size:31px;color:var(--white);letter-spacing:1px;text-shadow:0 2px 3px rgba(0,0,0,.3)}
.hero-sub{left:76px;top:161px;font-family:'Roboto',sans-serif;font-weight:700;font-size:21px;color:#111;letter-spacing:.5px}
.hero-btn{left:75px;top:207px;width:124px;height:29px;background:var(--green);color:#111;font-size:12.5px;display:flex;align-items:center;justify-content:center;border-radius:2px}
.panel{left:53px;top:296px;width:582px;height:726px;background:var(--panel)}
.about-h{left:72px;top:328px;font-size:17px;color:var(--green);font-weight:400}
.about-p{left:72px;top:359px;width:250px;font-size:7.6px;line-height:11.7px;color:#444}
.about-p p{margin-bottom:11px}
.about-img{left:350px;top:344px}
.divider{left:60px;top:507px;width:575px;height:1px;background:var(--muted)}
.feature{top:527px;width:139px;height:145px;text-align:center}
.feature.active{background:var(--white);border:1px solid #e2e2e2}
.feature svg{margin-top:20px}
.feature span{display:block;margin-top:6px;font-family:'Roboto',sans-serif;font-weight:700;font-size:14px;color:#1a1a1a}
.services{left:65px;top:718px;width:540px;height:26px;display:flex;align-items:center;justify-content:center}
.services .line{flex:1;height:1px;background:var(--muted)}
.services h2{font-family:'Roboto',sans-serif;font-weight:700;font-size:20px;color:var(--green);margin:0 10px}
.dots{display:flex;gap:3px;margin:0 4px}
.dots i{width:6px;height:6px;border-radius:50%;background:#222}
.dots i.g{background:var(--green)}
.tabs{left:85px;top:774px;display:flex;gap:0}
.tab{height:35px;padding:0 17px;display:flex;align-items:center;font-family:'Titillium Web',sans-serif;font-size:18px;font-weight:300;color:#222;letter-spacing:.8px}
.tab.on{background:var(--dark);color:var(--white);width:118px;justify-content:center}
.tab:nth-child(2){margin-left:14px;margin-right:18px}
.svc-p{left:82px;top:834px;width:500px;font-size:7.4px;line-height:10.6px;color:#333}
.svc-list{left:84px;top:897px;font-size:7.4px;color:#333}
.svc-list h4{font-size:7.4px;font-weight:700;margin-bottom:9px}
.svc-list li{list-style:none;line-height:13.8px}
.footer{left:0;top:1022px;width:688px;height:154px;background:var(--footer)}
.fcol{top:1034px;color:var(--white)}
.fcol h3{font-family:'Titillium Web',sans-serif;font-weight:600;font-size:11.5px;margin-bottom:10px;color:var(--white)}
.contact-row{display:flex;align-items:flex-start;gap:6px;font-size:7px;line-height:9px;margin-bottom:17px;color:var(--white)}
.tweet{font-size:6.4px;line-height:8.6px;margin-bottom:9px;color:#e6e6e6}
.tweet b{color:var(--white)}
.tweet em{font-style:normal;color:#aaa}
.tweet u{text-decoration:none;color:#9fd0f0}
.links li{list-style:none;font-size:7px;line-height:16px;color:var(--white)}
.follow p{width:124px;font-size:7px;line-height:10.4px;text-align:justify;color:var(--white)}
.social{display:flex;gap:5px;margin-top:14px}
.social i{width:16px;height:16px;background:#5a5a5a;border:1px solid #6e6e6e}
.bottom{left:0;top:1176px;width:688px;height:24px;background:var(--green);font-size:7px;color:#1a1a1a;display:flex;align-items:center;justify-content:space-between;padding:0 73px 0 74px}
</style>
</head>
<body>

<header class="header abs"></header>
<div class="brand abs"><span>VORTEL mobile</span><i class="dot"></i></div>
<div class="call abs"><b>Call Now:</b>
  <svg width="10" height="10" viewBox="0 0 24 24"><path fill="#8dc21f" d="M6.6 10.8c1.4 2.8 3.8 5.1 6.6 6.6l2.2-2.2c.3-.3.7-.4 1-.2 1.1.4 2.3.6 3.6.6.6 0 1 .4 1 1V20c0 .6-.4 1-1 1C10.6 21 3 13.4 3 4c0-.6.4-1 1-1h3.5c.6 0 1 .4 1 1 0 1.3.2 2.5.6 3.6.1.3 0 .7-.2 1z"/></svg>
  <span>555-01928374</span></div>

<nav class="nav abs">
  <a>HOME</a><a>ABOUT US</a><a>COMPANY PROFILE</a><a>THEY TRUST US</a><a>THE VORTEL TEAM</a><a>PARTNERS</a><a>CONTACT US</a>
</nav>

<div class="hero abs" role="img" aria-label="Business team meeting around a table in a bright office"></div>
<div class="hero-title abs">WORLD-CLASS</div>
<div class="hero-sub abs">ENTERPRISE SOLUTIONS</div>
<div class="hero-btn abs">More Information</div>

<section class="panel abs"></section>
<h1 class="about-h abs">VORTEL Mobile Exchange</h1>
<div class="about-p abs">
  <p>VORTEL Mobile Exchange is the combination of world-class enterprise solutions and an unrivaled global data network, creating the world's foremost provider of mobile enterprise applications and messaging. The result for our customers is unlimited potential.</p>
  <p>VORTEL Mobile Exchange with his Partners , has the resources, presence, knowledge, and experience to make any mobile strategy come to life. No other company comes close in terms of global reach, mobile enterprise software and services, or industry experience. VORTEL Mobile Exchange delivers messages to the point of action—helping customers get serious about mobile.</p>
</div>
<svg class="about-img abs" width="252" height="163" viewBox="0 0 252 163" role="img" aria-label="Hand holding a smartphone showing a news page, with a close-up circle">
  <defs>
    <linearGradient id="phg" x1="0" y1="0" x2="1" y2="1"><stop offset="0" stop-color="#6b5a44"/><stop offset="1" stop-color="#c9c2b5"/></linearGradient>
    <linearGradient id="hand" x1="0" y1="0" x2="1" y2="1"><stop offset="0" stop-color="#3a3a3a"/><stop offset=".6" stop-color="#d9b9a3"/><stop offset="1" stop-color="#c89a82"/></linearGradient>
  </defs>
  <path d="M160 0 L252 10 L220 163 L85 163 Z" fill="url(#hand)" opacity=".85"/>
  <circle cx="74" cy="76" r="74" fill="#fff"/>
  <circle cx="74" cy="76" r="70" fill="url(#phg)"/>
</svg>

<div class="divider abs"></div>

<div class="feature abs" style="left:49px"><svg width="74" height="74" viewBox="0 0 74 74"><circle cx="37" cy="37" r="37" fill="#8dc21f"/><g stroke="#fff" stroke-width="3" fill="#fff"><line x1="37" y1="22" x2="33" y2="36"/><line x1="33" y1="36" x2="25" y2="50"/><line x1="33" y1="36" x2="42" y2="44"/><line x1="42" y1="44" x2="49" y2="50"/><line x1="42" y1="44" x2="36" y2="50"/><circle cx="37" cy="22" r="4"/><circle cx="33" cy="36" r="4"/><circle cx="25" cy="50" r="4.5"/><circle cx="42" cy="44" r="4"/><circle cx="49" cy="50" r="4.5"/><circle cx="36" cy="51" r="3"/></g></svg><span>Advantage</span></div>
<div class="feature active abs" style="left:202px"><svg width="74" height="74" viewBox="0 0 74 74" style="margin-top:19px"><circle cx="37" cy="37" r="37" fill="#8dc21f"/><g stroke="#fff" stroke-width="3" fill="#fff"><line x1="37" y1="22" x2="33" y2="36"/><line x1="33" y1="36" x2="25" y2="50"/><line x1="33" y1="36" x2="42" y2="44"/><line x1="42" y1="44" x2="49" y2="50"/><line x1="42" y1="44" x2="36" y2="50"/><circle cx="37" cy="22" r="4"/><circle cx="33" cy="36" r="4"/><circle cx="25" cy="50" r="4.5"/><circle cx="42" cy="44" r="4"/><circle cx="49" cy="50" r="4.5"/><circle cx="36" cy="51" r="3"/></g></svg><span>Interoperability</span></div>
<div class="feature abs" style="left:352px;top:522px"><svg width="74" height="74" viewBox="0 0 74 74"><circle cx="37" cy="37" r="37" fill="#8dc21f"/><g stroke="#fff" stroke-width="3" fill="#fff"><line x1="37" y1="22" x2="33" y2="36"/><line x1="33" y1="36" x2="25" y2="50"/><line x1="33" y1="36" x2="42" y2="44"/><line x1="42" y1="44" x2="49" y2="50"/><line x1="42" y1="44" x2="36" y2="50"/><circle cx="37" cy="22" r="4"/><circle cx="33" cy="36" r="4"/><circle cx="25" cy="50" r="4.5"/><circle cx="42" cy="44" r="4"/><circle cx="49" cy="50" r="4.5"/><circle cx="36" cy="51" r="3"/></g></svg><span>Solution</span></div>
<div class="feature abs" style="left:499px;top:522px"><svg width="74" height="74" viewBox="0 0 74 74"><circle cx="37" cy="37" r="37" fill="#8dc21f"/><g stroke="#fff" stroke-width="3" fill="#fff"><line x1="37" y1="22" x2="33" y2="36"/><line x1="33" y1="36" x2="25" y2="50"/><line x1="33" y1="36" x2="42" y2="44"/><line x1="42" y1="44" x2="49" y2="50"/><line x1="42" y1="44" x2="36" y2="50"/><circle cx="37" cy="22" r="4"/><circle cx="33" cy="36" r="4"/><circle cx="25" cy="50" r="4.5"/><circle cx="42" cy="44" r="4"/><circle cx="49" cy="50" r="4.5"/><circle cx="36" cy="51" r="3"/></g></svg><span>Technology</span></div>

<div class="services abs">
  <div class="line"></div>
  <div class="dots"><i></i><i class="g"></i><i></i></div>
  <h2>Our Services</h2>
  <div class="dots"><i></i><i class="g"></i><i></i></div>
  <div class="line"></div>
</div>

<div class="tabs abs">
  <div class="tab on">Operator</div>
  <div class="tab">Brand &amp; Content</div>
  <div class="tab">Enterprise</div>
</div>

<p class="svc-p abs">VORTEL Mobile Exchange offers operators comprehensive services to facilitate the delivery of mobile data and content. Our global interoperability experience and capabilities are unrivaled. Providing operators with expanded reach—both to other networks and to greater subscriber content—is why so many operators select VORTEL Mobile Exchange as the vendor of choice.</p>

<div class="svc-list abs">
  <h4>VORTEL Mobile Exchange offers operators:</h4>
  <ul>
    <li>Operator-grade reliability</li>
    <li>High-availability and fault-tolerance that facilitates the seamless transmission of all types</li>
    <li>Message delivery across all mobile operators around the world</li>
    <li>A sophisticated infrastructure that features transcoding capabilities that traverse networks.</li>
    <li>Global service level agreements that ensure high network up-time</li>
    <li>Outstanding 24x7x365 customer support</li>
  </ul>
</div>

<footer class="footer abs"></footer>

<div class="fcol abs" style="left:75px">
  <h3>Contact us</h3>
  <div class="contact-row"><svg width="10" height="10" viewBox="0 0 24 24"><circle cx="12" cy="12" r="10.5" fill="none" stroke="#fff" stroke-width="2"/><path fill="#fff" d="M8.5 6.5l2 2-1 1.5c.8 1.6 1.9 2.7 3.5 3.5l1.5-1 2 2-1.3 1.6C11.5 16 8 12.5 7 8z"/></svg><span>555 0142 0199 (Phone)</span></div>
  <div class="contact-row"><svg width="11" height="10" viewBox="0 0 24 20"><rect x="2" y="7" width="20" height="10" rx="2" fill="#fff"/><rect x="6" y="2" width="12" height="6" fill="#fff"/><rect x="7" y="13" width="10" height="6" fill="#2e2e2e" stroke="#fff" stroke-width="1.5"/></svg><span>555 0142 0199 (Fax)</span></div>
  <div class="contact-row"><svg width="10" height="8" viewBox="0 0 24 18"><rect x="1" y="1" width="22" height="16" fill="#fff"/><path d="M1 1l11 9 11-9" fill="none" stroke="#2e2e2e" stroke-width="2"/></svg><span>hello@vortel-example.com</span></div>
  <div class="contact-row"><svg width="10" height="12" viewBox="0 0 20 24"><path fill="#fff" d="M10 0a8 8 0 0 0-8 8c0 6 8 16 8 16s8-10 8-16a8 8 0 0 0-8-8zm0 11a3 3 0 1 1 0-6 3 3 0 0 1 0 6z"/></svg><span>PO Box : 4120, Lorem City<br>ipsum dolor 0000</span></div>
</div>

<div class="fcol abs" style="left:215px">
  <h3>Latest Posts</h3>
  <div class="tweet"><b>Marla</b> <em>@northfeed</em><br>How to Download Photos from Feed<br>to... <u>vortel.link/Qa8kLm2x</u></div>
  <div class="tweet"><b>Marla</b> <em>@northfeed</em><br>How to Download Photos from Feed<br>to... <u>vortel.link/Qa8kLm2x</u></div>
  <div class="tweet"><b>Marla</b> <em>@northfeed</em><br>How to Download Photos from Feed<br>to... <u>vortel.link/Qa8kLm2x</u></div>
</div>

<div class="fcol abs" style="left:352px">
  <h3>About Us</h3>
  <ul class="links">
    <li>Investor</li><li>Careers</li><li>Terms &amp; Conditions of Services</li><li>Privacy Policy</li><li>Services Level Agreement</li><li>Master Commerical Agfreement</li>
  </ul>
</div>

<div class="fcol follow abs" style="left:480px">
  <h3>Follow Us</h3>
  <p>Lorem Ipsum is simply dummy text of the printing and typesetting industry. Lorem Ipsum has been the industry's standard dummy text ever since the 1500s,</p>
  <div class="social"><i></i><i></i><i></i><i></i><i></i><i></i></div>
</div>

<div class="bottom abs">
  <span>© Copyright 2015, Vortel | mobile, Inc. All rights reserved.</span>
  <span>Site Map | Legal | Privacy | Cookies</span>
</div>

</body>
</html>
```